Design a Flyer for Murmurly End of Financial Year Sale

Hi,

We require a End of Financial Year Sale Flyer made for our Murmurly page!

Our website is www.luvorn.com.au and we are going to have ALL packages 50% off on the 30th and 31st of June for 48 HOURS!

Some recent flyers from other freelancers are attached!

END OF FINANCIAL YEAR SALE
48 HOURS ONLY!

GET 50% OFF ALL YEARLY 12 MONTH SUBSCRIPTIONS!

TQW 12 MONTH SUBSCRIPTION NORMALLY $199.99 NOW JUST $99.99 (Picture of TQW)
HORSE RACING 12 MONTH SUBSCRIPTION NORMALLY $179.99 NOW JUST $89.99 (Picture of Horse)
GPV 12 MONTH SUBSCRIPTION NORMALLY $99.99 NOW JUST $49.99 (Picture of GPV)
SOCCER 12 MONTH SUBSCRIPTION NORMALLY $99.99 NOW JUST $49.99 (Picture Soccer)
HJC 12 MONTH SUBSCRIPTION NORMALLY $129.99 NOW JUST $64.99 (Picture of HJC)
TENNIS 12 MONTH SUBSCRIPTION NORMALLY $89.99 NOW JUST $44.99 (Picture of Tennis)
DXK 12 MONTH SUBSCRIPTION NORMALLY $89.99 NOW JUST $44.99 (Picture of DXK)
ALL SPORTS 12 MONTH SUBSCRIPTION NORMALLY $459.99 NOW JUST 229.99

PROMOCODE - EOFYS

BE QUICK LIMITED TIME ONLY!
WWW.LUVORN.COM.AU

```html
<!DOCTYPE html>
<html lang="en">
<head>
<meta charset="utf-8">
<title>Murmurly End of Financial Year Sale</title>
<link href="https://fonts.googleapis.com/css2?family=Titan+One&display=swap" rel="stylesheet">
<style>
  :root {
    --navy-deep: #08131f;
    --navy: #13283d;
    --navy-light: #1f3b57;
    --orange: #f5a623;
    --orange-deep: #e0781a;
    --white: #ffffff;
    --grey: #d9dde2;
    --pill-bg: #101e2d;
  }
  * { margin: 0; padding: 0; box-sizing: border-box; }
  html, body { width: 848px; height: 1200px; overflow: hidden; background: var(--navy-deep); }
  .flyer {
    position: relative;
    width: 848px; height: 1200px;
    overflow: hidden;
    background: radial-gradient(ellipse at 50% 40%, var(--navy-light) 0%, var(--navy) 45%, var(--navy-deep) 100%);
    font-family: "Titan One", "Arial Black", sans-serif;
    color: var(--white);
  }
  .brand {
    position: absolute; top: 96px; left: 0; width: 100%;
    text-align: center;
    font-size: 64px; letter-spacing: 2px;
    color: var(--white);
  }
  .headline {
    position: absolute; top: 254px; left: 0; width: 100%;
    text-align: center; line-height: 1.22; font-weight: 400;
  }
  .headline__main { font-size: 40px; color: var(--white); display: block; }
  .headline__sub { font-size: 40px; color: var(--orange); display: block; }
  .offer { position: absolute; width: 231px; }
  .offer__photo {
    width: 231px; height: 231px;
    border: 3px solid var(--orange);
    border-radius: 30px;
  }
  .offer__price {
    position: absolute; left: 0; width: 231px; height: 45px;
    display: flex;
    border: 3px solid var(--orange);
    border-radius: 10px;
    background: var(--pill-bg);
    overflow: hidden;
  }
  .offer__was, .offer__now {
    flex: 1; display: flex; align-items: center; justify-content: center;
    font-size: 21px;
  }
  .offer__was { color: var(--grey); text-decoration: line-through; border-right: 3px solid var(--orange); }
  .offer__now { color: var(--orange); }
  .row-1 { top: 380px; }
  .row-2 { top: 688px; }
  .row-1 .offer__price { top: 246px; }
  .row-2 .offer__price { top: 245px; }
  .col-1 { left: 66px; }
  .col-2 { left: 317px; }
  .col-3 { left: 566px; }
  .photo--football { background: linear-gradient(160deg, #6b5a52, #e8782a 55%, #2a3a5a); }
  .photo--racing { background: linear-gradient(160deg, #e9eef2, #2d5cc4 45%, #3a2a20 80%); }
  .photo--tqw { background: linear-gradient(160deg, #c45a5a, #6a4a30 45%, #e0b030 80%); }
  .photo--soccer { background: linear-gradient(180deg, #3a3f50, #c42a2a 45%, #3f8a3a 80%); }
  .photo--tennis { background: linear-gradient(160deg, #3a4a70, #3a8ae0 50%, #e8ecef); }
  .photo--hjc { background: linear-gradient(160deg, #3a2a2a, #f0eae6 45%, #8a4a2a 85%); }
  .promo {
    position: absolute; top: 1016px; left: 0; width: 100%;
    text-align: center; font-size: 24px; color: var(--white);
  }
  .footer-band { position: absolute; left: 0; top: 1040px; width: 848px; height: 160px; }
  .url {
    position: absolute; top: 1124px; left: 0; width: 100%;
    text-align: center; font-size: 29px; color: var(--white); letter-spacing: 1px;
  }
</style>
</head>
<body>
<main class="flyer">
  <div class="brand">LUVORN</div>

  <h1 class="headline">
    <span class="headline__main">END OF FINANCIAL YEAR</span>
    <span class="headline__sub">SALE 48 HOURS ONLY!!!</span>
  </h1>

  <section class="offer row-1 col-1">
    <div class="offer__photo photo--football" role="img" aria-label="Quarterback in orange jersey throwing a football"></div>
    <div class="offer__price"><span class="offer__was">$99.99</span><span class="offer__now">$49.99</span></div>
  </section>
  <section class="offer row-1 col-2">
    <div class="offer__photo photo--racing" role="img" aria-label="Jockey in blue silks riding a racehorse"></div>
    <div class="offer__price"><span class="offer__was">$179.99</span><span class="offer__now">$89.99</span></div>
  </section>
  <section class="offer row-1 col-3">
    <div class="offer__photo photo--tqw" role="img" aria-label="TQW player in brown and gold guernsey celebrating"></div>
    <div class="offer__price"><span class="offer__was">$199.99</span><span class="offer__now">$99.99</span></div>
  </section>

  <section class="offer row-2 col-1">
    <div class="offer__photo photo--soccer" role="img" aria-label="Soccer player in red kit striking the ball"></div>
    <div class="offer__price"><span class="offer__was">$99.99</span><span class="offer__now">$49.99</span></div>
  </section>
  <section class="offer row-2 col-2">
    <div class="offer__photo photo--tennis" role="img" aria-label="Tennis player in blue hitting a backhand"></div>
    <div class="offer__price"><span class="offer__was">$89.99</span><span class="offer__now">$44.99</span></div>
  </section>
  <section class="offer row-2 col-3">
    <div class="offer__photo photo--hjc" role="img" aria-label="HJC basketball player in white jersey dribbling"></div>
    <div class="offer__price"><span class="offer__was">$129.99</span><span class="offer__now">$64.99</span></div>
  </section>

  <p class="promo">PROMOCODE - EOFYs</p>

  <svg class="footer-band" viewBox="0 0 848 160">
    <defs>
      <linearGradient id="ctaFill" x1="0" y1="0" x2="0" y2="1">
        <stop offset="0" stop-color="#ffd23a"/>
        <stop offset="1" stop-color="#f07a18"/>
      </linearGradient>
      <path id="ctaCurve" d="M 95 90 Q 424 28 805 94"/>
    </defs>
    <path d="M 0 44 Q 424 -28 848 44 L 848 160 L 0 160 Z" fill="#07111b"/>
    <path d="M 0 44 Q 424 -28 848 44" fill="none" stroke="var(--orange)" stroke-width="3"/>
    <text font-family="Titan One, sans-serif" font-size="43" fill="url(#ctaFill)" text-anchor="middle">
      <textPath href="#ctaCurve" startOffset="50%">BE QUICK LIMITED TIME ONLY!</textPath>
    </text>
  </svg>

  <p class="url">WWW.LUVORN.COM.AU</p>
</main>
</body>
</html>
```